NEED A BUSINESS CARD FOR A NEW ELECTRICAL BUSINESS

HI I am after a new business card for my new electrical business I have a logo that I have attached its the one in blue, I would like that on the front and on the back my name- Leonard Pike, Email leonardpike@tallmesh.com, mobile 0491362047, licence no# vic 47819, nsw 591304k I wont something that is a stand out from the rest but at the same time is neat as being a new business I wont it to catch peoples eye on the front of the card I would like the logo and not much else.
And on the back as well I would like a slogan saying something like
Quality-Reliable-Service

Hi all on the back of the card I would like a little slogan like Quality-Reliable-Service something like that would be good thanks

Hi all the business card needs to have both these licence numbers on it                                                  VIC-47819 nsw-591304k

```html
<!DOCTYPE html>
<html lang="en">
<head>
<meta charset="utf-8">
<title>Leonard Pike Electrical — Business Card</title>
<link rel="stylesheet" href="https://fonts.googleapis.com/css2?family=Roboto:wght@400;700&display=swap">
<style>
  :root {
    --backdrop: #e9e6e1;
    --card: #2b2b2d;
    --card-edge: #1c1c1e;
    --blue: #1c74d0;
    --silver: #b9bcc0;
    --grey-text: #9a9da1;
  }
  * { margin: 0; padding: 0; box-sizing: border-box; }
  html, body {
    width: 1200px; height: 1000px; overflow: hidden;
    background: var(--backdrop);
    font-family: "Roboto", Arial, sans-serif;
  }
  .sheet {
    width: 1200px; height: 1000px;
    display: flex; flex-direction: column; align-items: center; justify-content: center; gap: 56px;
  }
  .card {
    width: 700px; height: 400px;
    background: var(--card);
    box-shadow: 0 6px 18px rgba(0,0,0,.28), 0 0 0 1px var(--card-edge);
    display: flex; flex-direction: column; align-items: center; justify-content: center;
  }
  .brand { display: flex; align-items: center; }
  .brand__square { background: var(--blue); flex: none; }
  .brand__name {
    color: var(--silver); font-weight: 700; text-transform: uppercase;
    letter-spacing: .03em; line-height: 1.02;
  }

  .card--front .brand { gap: 32px; }
  .card--front .brand__square { width: 150px; height: 150px; }
  .card--front .brand__name { font-size: 50px; }

  .card--back { text-align: center; }
  .card--back .brand { gap: 18px; }
  .card--back .brand__square { width: 64px; height: 64px; }
  .card--back .brand__name { font-size: 30px; text-align: left; }

  .contact { margin-top: 38px; }
  .contact__name {
    color: var(--blue); font-weight: 700; font-size: 26px;
    text-transform: uppercase; margin-bottom: 10px;
  }
  .contact__line { font-size: 20px; line-height: 1.5; color: var(--grey-text); }
  .contact__label { color: var(--blue); font-weight: 700; }
</style>
</head>
<body>
  <main class="sheet">
    <section class="card card--front" aria-label="Card front">
      <div class="brand">
        <span class="brand__square"></span>
        <span class="brand__name">Leonard Pike<br>Electrical</span>
      </div>
    </section>

    <section class="card card--back" aria-label="Card back">
      <div class="brand">
        <span class="brand__square"></span>
        <span class="brand__name">Leonard Pike<br>Electrical</span>
      </div>
      <div class="contact">
        <p class="contact__name">Leonard Pike</p>
        <p class="contact__line"><span class="contact__label">Mobile:</span> 0491362047</p>
        <p class="contact__line"><span class="contact__label">Email:</span> leonardpike@tallmesh.com</p>
        <p class="contact__line"><span class="contact__label">Licence No #</span> VIC 47819, NSW 591304K</p>
      </div>
    </section>
  </main>
</body>
</html>
```